Tarnby Group letterhead

Hi,

I need a letterhead template created for our business. This should be done in word format and A4 size. The images need to not move in the template ie when I am adding writing in etc. and should flow on when I get to a second page.

I have attached our logo templates below.

Other details to include on the letterhead somewhere are:

0438 915 267
Max@Tarnbyelectrical.example.au
PO Box 817 Marrowvale NSW 2190
ABN: 57 318 962 407

Thanks!

```html
<!DOCTYPE html>
<html lang="en">
<head>
<meta charset="utf-8">
<title>Tarnby Group Letterhead</title>
<link href="https://fonts.googleapis.com/css2?family=Montserrat:wght@600;700&family=Arimo:wght@400;700&display=swap" rel="stylesheet">
<style>
  :root {
    --backdrop: #d9d9d9;
    --paper: #ffffff;
    --ink: #2b2b2b;
    --body-ink: #4a4a4a;
    --charcoal: #1b1b1b;
    --signal-orange: #f05a12;
    --on-dark: #ffffff;
  }
  * { box-sizing: border-box; margin: 0; padding: 0; }
  html, body {
    width: 1200px; height: 1159px; overflow: hidden;
    background: var(--backdrop);
  }
  .letterhead {
    position: absolute; left: 220px; top: 42px;
    width: 760px; height: 1075px;
    background: var(--paper);
    box-shadow: 0 10px 30px rgba(0,0,0,.25);
    overflow: hidden;
    font-family: "Arimo", Arial, sans-serif;
    color: var(--body-ink);
  }
  .brand {
    position: absolute; top: 120px; left: 0; width: 100%;
    display: flex; justify-content: center; align-items: center; gap: 12px;
  }
  .brand-dot {
    width: 34px; height: 34px; border-radius: 50%;
    background: var(--signal-orange);
  }
  .brand-name {
    font-family: "Montserrat", Arial, sans-serif;
    font-weight: 700; font-size: 30px; letter-spacing: 1px;
    color: var(--charcoal); text-transform: uppercase;
  }
  .letter-body {
    position: absolute; top: 390px; left: 72px; right: 72px;
  }
  .salutation {
    font-family: "Montserrat", Arial, sans-serif;
    font-weight: 600; font-size: 17px; color: var(--ink);
    margin-bottom: 22px;
  }
  .letter-body p.para {
    font-size: 12.5px; line-height: 1.5; margin-bottom: 18px;
  }
  .closing {
    font-family: "Montserrat", Arial, sans-serif;
    font-weight: 600; font-size: 11px; color: var(--ink);
    margin-top: 34px;
  }
  .signature {
    width: 150px; height: 36px; margin-top: 22px;
    background: linear-gradient(90deg, #e6e6e6, #cfcfcf);
    border-radius: 4px;
  }
  .footer {
    position: absolute; left: 0; bottom: 0; width: 100%; height: 120px;
  }
  .footer-band { position: absolute; inset: 0; width: 100%; height: 100%; }
  .footer-contact {
    position: absolute; left: 56px; bottom: 22px;
    color: var(--on-dark); font-size: 14px; line-height: 1.5;
  }
  .footer-contact .row { display: flex; align-items: center; gap: 7px; }
  .footer-contact .label { color: var(--signal-orange); }
  .contact-icon { width: 12px; height: 12px; flex: none; display: block; }
  .footer-address {
    position: absolute; right: 48px; bottom: 34px;
    color: var(--on-dark); font-size: 14px; line-height: 1.45; text-align: right;
  }
</style>
</head>
<body>
  <main class="letterhead">
    <header class="brand">
      <span class="brand-dot"></span>
      <span class="brand-name">Tarnby Group</span>
    </header>

    <section class="letter-body">
      <p class="salutation">Dear Mr. Hollis,</p>
      <p class="para">Lorem ipsum dolor sit amet, consectetuer adipiscing elit, sed diam nonmmy nibh euismod tincidunt ut laor eet dolore magna aliquam erat volutpat. Ut wisi enim ad minim veniam, quis nostrud exerci tationmcorper suscipit lobortis nisl ut aliquip ex ea commodo consequat. Duis autem vel eum iriure dolor in hendrerit in vulputate velit esse molestie consequat, vel illum dolore eu feugiat</p>
      <p class="para">Rorem ipsum dolor sit amet, consectetuer adipiscing elit, sed diam nonmmy nibh euismod tincidunt ut laor eet dolore magna aliquam erat volutpat. Ut wisi enim ad minim veniam, quis nostrud exerci tationmcorper suscipit lobortis nisl ut aliquip ex ea commodo consequat. Duis autem vel eum iriure dolor in hendrerit in vulputate velit esse molest</p>
      <p class="para">Dorem ipsum dolor sit amet, consectetuer adipiscing elit, sed diam nonmmy nibh euismod tincidunt ut laor eet dolore magna aliquam erat volutpat. Ut wisi enim ad minim veniam, quis nostrud exerci tationmcorper suscipit lobortis nisl ut aliquip ex ea commodo consequat. Duis autem vel eum iriure dolor in hendrerit in suscipit lobortis nisl ut aliquip ex ea commodo consequat. Duis autem vel eum iriure dolor in hendrerit in vulputate velit esse molestie consequat, vel illum</p>
      <p class="para">Sorem ipsum dolor sit amet, consectetuer adipiscing elit, sed diam nonmmy nibh euismod tincidunt ut laor eet dolore magna aliquam erat volutpat. Ut wisi enim ad minim veniam, quis nostrud exerci tationmcorper suscipit lobortis nisl ut aliquip ex ea commodo consequat. Duis autem vel eum iriure dolor in</p>
      <p class="closing">Sincerely,</p>
      <div class="signature" role="img" aria-label="Handwritten signature"></div>
    </section>

    <footer class="footer">
      <svg class="footer-band" viewBox="0 0 760 120" preserveAspectRatio="none" aria-hidden="true">
        <rect x="0" y="0" width="760" height="120" fill="var(--charcoal)"/>
        <polygon points="420,0 760,0 760,120 395,120" fill="var(--signal-orange)"/>
      </svg>
      <div class="footer-contact">
        <div class="row">
          <svg class="contact-icon" viewBox="0 0 24 24" aria-hidden="true"><path fill="var(--signal-orange)" d="M6.6 10.8a15.1 15.1 0 0 0 6.6 6.6l2.2-2.2a1 1 0 0 1 1-.25 11.4 11.4 0 0 0 3.6.57 1 1 0 0 1 1 1V20a1 1 0 0 1-1 1A17 17 0 0 1 3 4a1 1 0 0 1 1-1h3.5a1 1 0 0 1 1 1c0 1.25.2 2.45.57 3.57a1 1 0 0 1-.25 1z"/></svg>
          <span>0438 915 267</span>
        </div>
        <div class="row">
          <svg class="contact-icon" viewBox="0 0 24 24" aria-hidden="true"><path fill="var(--signal-orange)" d="M2 5h20v14H2zm2 2v.5l8 5 8-5V7z"/></svg>
          <span>Max@Tarnbyelectrical.example.au</span>
        </div>
        <div class="row"><span class="label">ABN:</span><span>57 318 962 407</span></div>
      </div>
      <div class="footer-address">PO Box 817<br>Marrowvale NSW 2190</div>
    </footer>
  </main>
</body>
</html>
```